www.tarnebluvion.net

Hi,
UPDATE: Logo attached
TAG LINE NEW: OBITUARIES * CONDOLENCE NOTES
MULTIMEDIA MEMORIAL
Please refer to our existing site for more explanation of who we are?
We are a global data collecting portal site managing the Jewish funeral industry where users:
a) family and freinds in grief or "ancestry" searching persons
b) chevra kadisha's (funeral parlor)
c) current and historic cemetaries
d) Jewish Media Partners
arrive and choose a function (category):
in order to:
- upload a basic listing (FREE)
- upload/upgrade a multimedia listing (PAID)
- or search for a listing
of a deceased person (potentially millions of entries)
The functions (or categories) are accessed after the user:
Chooses their global location of search by
"Choose your Location" ie: Australia/NZ (which country?)
and allows the USER to choose a category function such as:
GROUP A (Local Info) GROUP B (Soul Search)
Chevra Kadisha Funerals (within 7 days)
Cemetaries Recently Deceased (up to 12mth)
Stonemasons Soul Search (after 1 year)
Jewish Media Partners
GROUP C (Jewish Death & Mourning Customs)
The way of Jewish burial
3000 y/old customs
When will Moshiach Come ?
Will I see my loved one again?
AIM:
To utilize existing logo and side menus (Member, Main & Resources) to create a user freindly and simpler friendly landing page, warmer and more softer for viewers.
To create logo buttons for the service catogories:
A, B & C and separate sub catagories
The MAIN AIM is to offer users opportunity to upload (LOG-IN required)
a) NEW basic FREE listing
b) NEW Multi-media PAID listing
SUMMARY:
1) User arrives at landing paid and sees global map, where he/she must choose the location in order to localize his data search
At this point, he/she can see what the site offers by the side MAIN, menu and icon function/catagories
(ie: Soul Search, New Basic Listing, Multimedia Listing)
2) After arriving at location (ie: Australia/NZ), the user then chooses the sub-function icon:
A- Local Funeral Service Info (Chevra Kadisha, Cemetary etc)
B- Soul Search (Funeral,Recently Deceased, Soul Search)
C- Jewish Death & Mourning Cutoms
Updates
Hi
Reason: Because of the holidays, we are happy to extend the deadline....
happy times
Target Market(s)
Family persons (Guest Member) & Industry (Members)
Industry/Entity Type
Industry
Requirements
Must have
- Style : Simple, Neat & Easy to Navigate
Icons: for each catagory/function
Colors; natural
-
Ability to bring inspiration, hope, light and healing to a difficult subject matter. (site look)
-
Education a profoundly deep 3000 y/old historically rich and mystic tradition to a wide audience
-
Allow children to access and upload data about grandparents etc
-
To promote on landing page the Invitation of local Chevra Kadisha's (funeral parlors), who have no web exposure, to get involved and LOG-IN and upload basic or multimedia listings.
(ie: please Register your local Chevra Kadisha here)
-
To promote on the landing page sample listings (Recently Deceased), to show look/feel of listings

```html
<!DOCTYPE html>
<html lang="en">
<head>
<meta charset="utf-8">
<title>tarnebluvion.net – Home</title>
<link href="https://fonts.googleapis.com/css2?family=PT+Sans:wght@400;700&family=Arimo:wght@400;700&family=Tinos:ital@1&display=swap" rel="stylesheet">
<style>
:root{
  --sky-top:#4f93c9;
  --sky-mid:#a9d0ec;
  --sky-low:#eef6fb;
  --nav:#1f5473;
  --nav-active:#173f58;
  --nav-text:#d4e6f1;
  --frame:#a9d3e6;
  --accent:#2b82b5;
  --link:#2f6f9c;
  --text:#3b3b3b;
  --side-bg:#edf6fa;
  --side-head-top:#6d9ebd;
  --side-head-bot:#2f6688;
  --border:#cfe0ea;
  --footer:#3b6f92;
  --footer-deep:#2f5f80;
  --footer-text:#e8f1f7;
  --white:#ffffff;
}
*{box-sizing:border-box;margin:0;padding:0}
html,body{width:889px;height:1200px;overflow:hidden}
body{position:relative;background:var(--white);font-family:"Arimo",Arial,sans-serif;color:var(--text)}
.sky{position:absolute;left:0;top:0;width:889px;height:400px;
  background:radial-gradient(ellipse at 15% 25%,rgba(255,255,255,.85),transparent 40%),
  radial-gradient(ellipse at 80% 10%,rgba(255,255,255,.7),transparent 35%),
  radial-gradient(ellipse at 60% 70%,rgba(255,255,255,.6),transparent 45%),
  linear-gradient(var(--sky-top),var(--sky-mid) 55%,var(--sky-low));}
.brand{position:absolute;left:360px;top:58px;width:170px;display:flex;align-items:center;gap:6px;
  font-family:"PT Sans",sans-serif;font-size:19px;color:#1f4f6b}
.brand-dot{width:12px;height:12px;border-radius:50%;background:#e08a2c;flex:none}
.main-nav{position:absolute;left:47px;top:120px;width:806px;height:28px;background:var(--nav);display:flex;padding-left:21px}
.main-nav a{font-family:"PT Sans",sans-serif;font-size:12px;color:var(--nav-text);text-decoration:none;
  height:28px;line-height:28px;padding:0 0 0 12px;border-right:1px solid #2f6a8c}
.main-nav a.active{background:var(--nav-active);color:#fff}
.hero{position:absolute;left:45px;top:148px;width:808px;height:192px;background:var(--frame);padding:4px 5px}
.hero-photo{width:100%;height:100%;background:linear-gradient(180deg,#dfe7c8 0%,#bccf7a 45%,#6f9a2a 100%)}
.punch{position:absolute;right:5px;top:72px;width:258px;height:66px;background:rgba(255,255,255,.55);
  font-family:"Tinos",serif;font-style:italic;font-size:18px;line-height:23px;color:#1f2a2f;text-align:right;padding:10px 48px 0 0}
.dots{position:absolute;left:412px;top:342px;display:flex;gap:3px}
.dots i{width:9px;height:9px;border-radius:50%;background:var(--nav)}
.regions{position:absolute;left:42px;top:356px;width:811px;height:32px;background:#fff;border:1px solid var(--border);display:flex}
.regions a{font-family:"PT Sans",sans-serif;font-size:14px;color:#333;text-decoration:none;line-height:30px;text-align:center;border-right:1px solid var(--border)}
.panel{position:absolute;left:42px;top:388px;width:811px;height:640px;border:1px solid var(--border);border-top:none;background:#fff}
.sidebar{position:absolute;left:47px;top:398px;width:193px;height:622px;background:linear-gradient(90deg,var(--side-bg),#f8fcfe)}
.side-head{width:186px;background:linear-gradient(var(--side-head-top),var(--side-head-bot));color:#fff;
  font-family:"PT Sans",sans-serif;font-size:14px;padding:4px 12px;border-radius:2px;line-height:16px}
.side-list{list-style:none;padding:8px 0 10px 14px}
.side-list li{font-size:11px;line-height:13px;margin-bottom:5.5px;padding-left:19px;position:relative;color:#222}
.side-list li::before{content:"";position:absolute;left:0;top:3px;width:13px;height:6px;border:1.5px solid #2d5d7c;border-radius:6px 6px 6px 2px}
.login{padding:14px 0 0 11px;font-size:12px;color:#222}
.login label{display:block;margin-bottom:2px}
.login .field{width:159px;height:17px;border:1px solid #aab;border-radius:9px;font-size:10px;color:#999;padding:2px 8px;margin-bottom:6px}
.login .remember{font-size:10px;text-align:right;padding-right:18px;margin-top:2px}
.login .remember b{display:inline-block;width:9px;height:9px;background:#222;vertical-align:-1px;margin-right:3px}
.login .submit{display:inline-block;margin-top:8px;margin-left:5px;background:#000;color:#fff;border-radius:9px;font-size:10px;padding:2px 14px}
.content{position:absolute;left:262px;top:402px;width:575px}
.section-title{font-family:"PT Sans",sans-serif;font-size:19px;color:var(--accent);padding-left:34px;position:relative;border-bottom:1px solid #c7dbe7;height:26px}
.section-title::before{content:"";position:absolute;left:2px;top:5px;width:26px;height:14px;background:#8aa6b8;border-radius:50% 50% 50% 10%}
.copy{font-size:11px;line-height:12.8px;padding:8px 0 0 3px;color:#3a3a3a}
.copy .lead{text-decoration:underline}
.map{margin:18px 0 8px 0;width:503px;height:228px;background:linear-gradient(135deg,#e8f0c9,#b7cf72 40%,#efe79a 65%,#d7e4b2);border:5px solid #eee}
.links{list-style:none;padding:10px 0 0 0}
.links li{font-size:11px;line-height:16.5px;padding-left:15px;position:relative}
.links li::before{content:"";position:absolute;left:2px;top:5px;width:7px;height:7px;border-radius:50%;background:#000}
.links a{color:var(--link)}
.footer{position:absolute;left:0;top:1027px;width:889px;height:173px;background:var(--footer);color:var(--footer-text)}
.footer h3{font-family:"PT Sans",sans-serif;font-weight:400;font-size:14px;margin-bottom:8px}
.footer ul{list-style:none;font-size:10px;line-height:12.3px}
.fcol{position:absolute;top:16px}
.social{display:flex;gap:3px;margin-top:16px}
.social span{width:18px;height:18px;background:#7aa8c8;border:1px solid #cfe2ee}
.legal{position:absolute;left:0;bottom:0;width:889px;height:23px;background:var(--footer-deep);font-size:10px;text-align:right;padding:6px 38px 0 0}
</style>
</head>
<body>
<div class="sky"></div>
<div class="brand"><span class="brand-dot"></span>tarnebluvion.net</div>

<nav class="main-nav">
  <a class="active" style="width:85px">MAIN PAGE</a>
  <a style="width:107px;padding-left:31px">ABOUT US</a>
  <a style="width:95px;padding-left:23px">SERVICES</a>
  <a style="width:64px;padding-left:21px">VEDIOS</a>
  <a style="width:157px;padding-left:105px;border:none">BLOG</a>
  <a style="width:107px;padding-left:21px">PARTNERS</a>
  <a style="width:91px;padding-left:30px">GALLERY</a>
  <a style="width:110px;padding-left:20px;border:none">CONTACT INFO</a>
</nav>

<div class="hero">
  <div class="hero-photo" role="img" aria-label="Children holding sunflowers in a summer meadow"></div>
  <div class="punch">YOUR PUNCH LINES<br>&nbsp;&nbsp;&nbsp;&nbsp;GOES HERE.</div>
</div>
<div class="dots"><i></i><i></i><i></i><i></i></div>

<div class="regions">
  <a style="width:124px">Australia/NZ</a><a style="width:72px">Canada</a><a style="width:106px">United States</a><a style="width:61px">Israel</a><a style="width:70px">Europe</a><a style="width:43px">UK</a><a style="width:56px">Asia</a><a style="width:184px">Central and South America</a><a style="width:93px;border:none">Africa</a>
</div>

<div class="panel"></div>

<aside class="sidebar">
  <div class="side-head">Local Informations</div>
  <ul class="side-list">
    <li>Go to Main Page</li><li>About Our Company</li><li>Our Services</li><li>Photos &amp; Blog</li><li>Contact Us</li><li>Features</li>
  </ul>
  <div class="side-head">Soul Search</div>
  <ul class="side-list" style="padding-left:8px">
    <li>Chevra Kadisha Funerals (within 7 days)</li><li>Cemetaries Recently De­ceased (up to 12mth)</li><li>Stonemasons Soul Search (after 1 year)</li><li>Jewish Media Partners</li>
  </ul>
  <div class="side-head">Jewish Death &amp; Mourning Customs</div>
  <ul class="side-list" style="padding-left:8px">
    <li>The way of Jewish burial</li><li>3000 y/old customs</li><li>When will Moshiach Come ?</li><li>Will I see my loved one again?</li>
  </ul>
  <div class="side-head">Please Log In</div>
  <div class="login">
    <label>Your Name</label><div class="field">type your name</div>
    <label>Password</label><div class="field">type your password</div>
    <div class="remember"><b></b>forget password</div>
    <span class="submit">submit</span>
  </div>
</aside>

<main class="content">
  <h2 class="section-title">Welcome to our website home page</h2>
  <p class="copy"><span class="lead">Brightloom eSolutions is a web service company, offering a wide range of services which range from design­ing and development, that is covering almost all the fields</span> in the best possible way. To be the best we know what and how to present beautifully the working of the client’s need and their advantages be highlighted. We act in accordance with the Industry certified processes to deliver the best to our clients all over the world. Over years we have built a strong reputation in providing website design and web development services.<br><br>Thus, Wanna get ahead in the competition with other websites…. Brightloom esolutions provide you with an attractive and most convincing website to enhance your marketing goals.<br>The only way to success is through the right path and that’s what we provide you. None of the other compa­nies has the result we do. So stick to the best that’s how you will be the best don’t opt for the second best. Our expertise does not limit itself to web development</p>
  <h2 class="section-title" style="margin-top:26px">Please choose your region</h2>
  <div class="map" role="img" aria-label="World map with time zones for choosing a region"></div>
  <p class="copy" style="padding:0">Tarnebluvion.net is the global Jewish community's sacred burial society's website and resource portal, for data collation of personal media (obituaries, condolence comments, photos &amp; video), relating to Jewish per­sons who have passed on, for use by service providers and relatives today and in successive generations. Here you can find details information about your local Chevra Kadisha and support services, such as Cem­eteries, Stonemasons and Jewish Newspapers. Other categories include:</p>
  <ul class="links">
    <li><a>Funerals and Minyans - during the shiva period (7 days);</a></li>
    <li><a>Recently Deceased - during the shloshim period (30 days); and</a></li>
    <li><a>Soul search - after the shloshim period.</a></li>
  </ul>
</main>

<footer class="footer">
  <div class="fcol" style="left:47px">
    <h3>Resources</h3>
    <ul><li>What is the "Kaddish"?</li><li>Yarzeit Reminder email</li><li>Articles</li><li>US Council of Burial Societies</li><li>Mizrah.org (customs)</li><li>Kollel Beit Avot (Hevron)</li><li>Nechama</li><li>Jewish Funeral Guild of America</li></ul>
  </div>
  <div class="fcol" style="left:295px">
    <h3>Connect With Us</h3>
    <ul style="padding-left:3px"><li>Linkwell</li><li>Chirper</li><li>Friendline</li><li>Rss</li></ul>
    <div class="social"><span></span><span></span><span></span><span></span></div>
  </div>
  <div class="fcol" style="left:464px">
    <h3>Partners</h3>
    <ul><li>Patner name goes here</li><li>Patner second goes here</li><li>thrid goes here</li><li>fourth parner goes here</li><li>Parner fifith goes</li></ul>
  </div>
  <div class="legal">copyright © 2011 &nbsp;company name &nbsp;All right reserved</div>
</footer>
</body>
</html>
```